Online Dating Ebook Needs an Amazing Cover Design

This is a cover for an online dating ebook that will go online to the Pagewell store and will have a large audience. It is targeted primarily to men and is written from the perspective of a Strategy Consultant

The cover needs to be elegant, seductive and eye catching but not overbearing or cheesy. No pornography, outright nudity, etc. It should draw the eye.

The title is

"Master Web Romance" with the subtitle "A Business Advisor's Handbook"

The author's name would need to be Mark Tellby.

Feel free to send emails asking for feedback on your designs so we can work on many versions

Target Market(s)

Target market is 18-40 year old single males who will be doing online dating

Industry/Entity Type

Dating

Requirements
Must have
• 1)Must be given a .jpg and vector file.

2) Must be 900 pixel Height and 600 pixel width.

3)Need a 300 dpi and 72 dpi version

4) Author's name as Mark Tellby

```html
<!DOCTYPE html>
<html lang="en">
<head>
<meta charset="utf-8">
<title>Master Web Romance — Mark Tellby</title>
<link href="https://fonts.googleapis.com/css2?family=Cinzel:wght@400&family=Ubuntu:wght@400&display=swap" rel="stylesheet">
<style>
  :root {
    --page: #ffffff;
    --navy-night: #050f22;
    --navy-deep: #0b1f3f;
    --navy: #17345f;
    --steel: #5b80ae;
    --glow: #f4f7fb;
    --ink-light: #ffffff;
  }
  html, body {
    margin: 0;
    padding: 0;
    width: 960px;
    height: 1200px;
    overflow: hidden;
    background: var(--page);
  }
  .book-cover {
    position: absolute;
    left: 190px;
    top: 166px;
    width: 566px;
    height: 848px;
    overflow: hidden;
    background: var(--navy-deep);
  }
  .cover-art {
    position: absolute;
    inset: 0;
    width: 566px;
    height: 848px;
    display: block;
  }
  .cover-text {
    position: absolute;
    left: 0;
    width: 100%;
    text-align: center;
    color: var(--ink-light);
    margin: 0;
    line-height: 1;
    white-space: nowrap;
  }
  .title-main {
    top: 536px;
    font-family: "Cinzel", serif;
    font-weight: 400;
    font-size: 82px;
    letter-spacing: 7px;
    padding-left: 7px;
  }
  .title-sub {
    top: 624px;
    font-family: "Ubuntu", sans-serif;
    font-weight: 400;
    font-size: 60px;
  }
  .subtitle {
    top: 702px;
    font-family: "Ubuntu", sans-serif;
    font-size: 16px;
  }
  .author {
    top: 797px;
    font-family: "Ubuntu", sans-serif;
    font-size: 19px;
  }
</style>
</head>
<body>
  <article class="book-cover">
    <svg class="cover-art" viewBox="0 0 566 848" role="img" aria-label="Photo of a glowing white silhouette of a couple walking hand in hand in front of a dark blue screen of app icons, with tall grass along the bottom">
      <defs>
        <linearGradient id="backdrop" x1="0" y1="0" x2="0.3" y2="1">
          <stop offset="0" stop-color="var(--navy-night)"/>
          <stop offset="0.35" stop-color="var(--navy)"/>
          <stop offset="0.6" stop-color="#234a7c"/>
          <stop offset="1" stop-color="var(--navy-deep)"/>
        </linearGradient>
        <linearGradient id="figure-glow" x1="0" y1="0" x2="0" y2="1">
          <stop offset="0" stop-color="var(--glow)"/>
          <stop offset="0.35" stop-color="#dfe6f0"/>
          <stop offset="0.7" stop-color="var(--steel)" stop-opacity="0.8"/>
          <stop offset="1" stop-color="var(--navy)" stop-opacity="0"/>
        </linearGradient>
        <linearGradient id="ground" x1="0" y1="0" x2="0" y2="1">
          <stop offset="0" stop-color="var(--navy-deep)" stop-opacity="0"/>
          <stop offset="1" stop-color="var(--navy-night)" stop-opacity="0.9"/>
        </linearGradient>
        <filter id="soften" x="-30%" y="-30%" width="160%" height="160%">
          <feGaussianBlur stdDeviation="14"/>
        </filter>
      </defs>
      <rect class="art-backdrop" width="566" height="848" fill="url(#backdrop)"/>
      <g class="art-couple-glow" filter="url(#soften)">
        <rect x="88" y="150" width="160" height="620" rx="80" fill="url(#figure-glow)"/>
        <rect x="332" y="136" width="206" height="640" rx="100" fill="url(#figure-glow)"/>
      </g>
      <rect class="art-ground" y="600" width="566" height="248" fill="url(#ground)"/>
    </svg>
    <h1 class="cover-text title-main">MASTER</h1>
    <p class="cover-text title-sub">Web Romance</p>
    <p class="cover-text subtitle">A Business Advisor's Handbook</p>
    <p class="cover-text author">by Mark Tellby</p>
  </article>
</body>
</html>
```